Wandrift: Travel business card redesign

We need a clean elegant look for our cards featuring blue and orange. Look should communicate a sense of strong design and seem uncluttered. The company is Wandrift which means drift to wander. As in every trip is an drift to wander. Feel free to reinvent the logo or just tweak it. Colors should be blue like Caribbean waters and a saturated orange. Keep it clean and simple.
Please match the information in the sample uploaded but the sample is horrible -- a non-starter -- use for information only. also please add managing director to my name as title

Target Market(s)
potential clients, hotels, trade publications
Industry/Entity Type
Travel Industry
Contact Information for Business Card
as above
Requirements
Must have
- Font should be century gothic. Colors below are close but a but prefer lighter in each case.

```html
<!DOCTYPE html>
<html lang="en">
<head>
<meta charset="utf-8">
<title>Wandrift – Business Card</title>
<link rel="stylesheet" href="https://fonts.googleapis.com/css2?family=Questrial&display=swap">
<style>
  :root {
    --backdrop: #1e1e1f;
    --orange: #ee8a2a;
    --orange-light: #f2a23c;
    --orange-deep: #e97e22;
    --blue: #3d9fd6;
    --ink: #4a4a4a;
    --paper: #ffffff;
    --card-radius: 30px;
  }
  * { box-sizing: border-box; margin: 0; padding: 0; }
  html, body {
    width: 1200px; height: 1000px; overflow: hidden;
    background: var(--backdrop);
    font-family: "Questrial", "Century Gothic", sans-serif;
  }
  .stage { position: relative; width: 1200px; height: 1000px; }

  .card {
    position: absolute; width: 560px; height: 320px;
    border-radius: var(--card-radius); overflow: hidden;
    box-shadow: 0 18px 40px rgba(0,0,0,.55);
  }

  /* Front */
  .card--front {
    left: 110px; top: 110px;
    background: linear-gradient(135deg, var(--orange-deep) 0%, var(--orange) 50%, var(--orange-light) 100%);
    color: var(--paper);
  }
  .card--front .brand {
    position: absolute; left: 0; right: 0; top: 112px; text-align: center;
  }
  .brand__name { font-size: 52px; font-weight: 400; letter-spacing: -1px; line-height: 1; }
  .brand__tagline { font-size: 19px; letter-spacing: 1px; margin-top: 4px; }
  .card--front .slogan {
    position: absolute; left: 0; right: 0; bottom: 34px; text-align: center;
    font-size: 15px; letter-spacing: 1px; opacity: .95;
  }

  /* Back */
  .card--back { left: 530px; top: 540px; background: var(--paper); }
  .card--back .brand {
    position: absolute; right: 36px; top: 28px; text-align: right;
  }
  .card--back .brand__name { color: var(--orange); font-size: 40px; }
  .card--back .brand__tagline { color: var(--blue); font-size: 15px; margin-top: 2px; }

  .rule {
    position: absolute; left: 196px; right: 36px; top: 118px;
    height: 1px; background: var(--blue);
  }
  .edge-tab {
    position: absolute; left: 0; top: 176px; width: 12px; height: 36px;
    background: var(--orange); border-radius: 0 6px 6px 0;
  }
  .person { position: absolute; left: 30px; top: 168px; }
  .person__name { color: var(--orange); font-size: 30px; line-height: 1.05; font-weight: 400; }
  .person__title { color: var(--blue); font-size: 15px; letter-spacing: .3px; }

  .contacts { position: absolute; left: 30px; top: 232px; list-style: none; }
  .contacts li {
    display: flex; align-items: center; gap: 10px;
    color: var(--ink); font-size: 15px; line-height: 22px;
  }
  .contacts svg { width: 12px; height: 12px; fill: var(--orange); flex: none; }

  .address {
    position: absolute; right: 36px; top: 140px; text-align: right;
    color: var(--ink); font-size: 14px; line-height: 19px;
  }
  .web-tab {
    position: absolute; right: 0; bottom: 0; width: 170px; height: 54px;
    background: var(--orange); border-top-left-radius: 28px;
    color: var(--paper); font-size: 18px;
    display: flex; align-items: center; justify-content: center;
  }
</style>
</head>
<body>
<main class="stage">

  <section class="card card--front" aria-label="Card front">
    <div class="brand">
      <div class="brand__name">wandrift</div>
      <div class="brand__tagline">drift to wander</div>
    </div>
    <p class="slogan">a first in service company</p>
  </section>

  <section class="card card--back" aria-label="Card back">
    <div class="brand">
      <div class="brand__name">wandrift</div>
      <div class="brand__tagline">drift to wander</div>
    </div>
    <div class="rule"></div>

    <p class="address">1470 Harbor Crest Way<br>Coral Bay, 90417</p>

    <div class="edge-tab"></div>
    <div class="person">
      <h1 class="person__name">Leo Marren</h1>
      <p class="person__title">Managing Director</p>
    </div>

    <ul class="contacts">
      <li>
        <svg viewBox="0 0 24 24" aria-hidden="true"><path d="M6.6 10.8a15.1 15.1 0 0 0 6.6 6.6l2.2-2.2a1 1 0 0 1 1-.25 11.4 11.4 0 0 0 3.6.57 1 1 0 0 1 1 1V20a1 1 0 0 1-1 1A17 17 0 0 1 3 4a1 1 0 0 1 1-1h3.5a1 1 0 0 1 1 1c0 1.25.2 2.45.57 3.57a1 1 0 0 1-.25 1z"/></svg>
        877.55.(926374)
      </li>
      <li>
        <svg viewBox="0 0 24 24" aria-hidden="true"><path d="M7 1h10a2 2 0 0 1 2 2v18a2 2 0 0 1-2 2H7a2 2 0 0 1-2-2V3a2 2 0 0 1 2-2zm0 3v14h10V4zm5 15.5a1.2 1.2 0 1 0 0 2.4 1.2 1.2 0 0 0 0-2.4z"/></svg>
        323.555.0148
      </li>
      <li>
        <svg viewBox="0 0 24 24" aria-hidden="true"><path d="M6 2h9l3 3v5H6zM3 11h18a2 2 0 0 1 2 2v7a2 2 0 0 1-2 2H3a2 2 0 0 1-2-2v-7a2 2 0 0 1 2-2zm3 3v2h4v-2z"/></svg>
        310.555.0192
      </li>
    </ul>

    <div class="web-tab">wandrift.com</div>
  </section>

</main>
</body>
</html>
```